First North America Product Category Rule

8 x 10 foot booth design for a stretch fabric wrap-around. The booth will be used in a very small exhibit area for 150 attendees. It is for the packaging industry focused on the environment. This booth graphic is NOT about our company, but to promote participation in a project we are sponsoring. The project is to develop the first North American Packaging Category Rule, so the booth is to invite conference attendees to join our effort. Production specifications are attached.

Target Market(s)

Zenith 400, Sustainability Directors, Packaging Engineers

Industry/Entity Type

Packaging; Environment

Font styles to use
Sans Serif

Requirements
Must have
• An Eye-Catching or Intriguing Image/Graphics/Letter Treatment
Should not have
• Nothing too bright or garish. All text should be above waist height (No text below the 36-40" mark)

```html
<!DOCTYPE html>
<html lang="en">
<head>
<meta charset="utf-8">
<title>Enlisting Stakeholder Participation – Protective Packaging PCR</title>
<link href="https://fonts.googleapis.com/css2?family=Bitter:ital,wght@0,400;0,500;0,700;1,600&family=Fjalla+One&family=Bebas+Neue&display=swap" rel="stylesheet">
<style>
  :root {
    --teal: #2fb3a8;
    --teal-deep: #1f8f95;
    --blue: #3f5fb0;
    --navy: #1b2638;
    --ink: #111111;
    --paper: #f7f7f7;
    --badge: #e4df8e;
    --white: #ffffff;
  }
  * { margin: 0; padding: 0; box-sizing: border-box; }
  html, body { width: 1200px; height: 840px; overflow: hidden; background: var(--paper); }
  .booth-wall { position: relative; width: 1200px; height: 840px; overflow: hidden;
    background: linear-gradient(115deg, #ffffff 0%, #f2f2f2 60%, #e9e9e9 100%);
    font-family: "Bitter", Georgia, serif; color: var(--ink); }
  .layer { position: absolute; inset: 0; width: 1200px; height: 840px; }

  .signup-badge { position: absolute; left: 48px; top: 14px; width: 128px; }
  .signup-badge__strip { height: 12px; background: var(--teal); }
  .signup-badge__card { background: var(--badge); height: 108px; display: flex; align-items: center; justify-content: center;
    text-align: center; font-family: "Bebas Neue", Impact, sans-serif; font-size: 46px; line-height: 0.9; color: var(--teal-deep); }
  .signup-badge__roll { width: 128px; height: 100px; border-radius: 0 0 20px 46px;
    background: linear-gradient(160deg, var(--blue), var(--teal)); }

  .headline { position: absolute; right: 645px; top: 58px; text-align: right; color: var(--teal);
    font-weight: 700; font-size: 54px; line-height: 1.24; white-space: nowrap; }

  .rule { position: absolute; left: 42px; width: 650px; height: 3px; background: var(--ink); }
  .rule--top { top: 328px; }
  .rule--bottom { top: 548px; }

  .title-block { position: absolute; right: 508px; top: 342px; text-align: right; white-space: nowrap; }
  .title-block__kicker { font-style: italic; font-weight: 600; font-size: 34px; }
  .title-block__main { font-family: "Fjalla One", "Arial Narrow", sans-serif; font-size: 54px; line-height: 1.25; font-weight: 400; }

  .sponsor { position: absolute; left: 408px; top: 588px; font-weight: 700; font-size: 26px; line-height: 1.3; }

  .quote { position: absolute; left: 790px; top: 606px; width: 370px; text-align: center; color: var(--white);
    font-family: "Fjalla One", "Arial Narrow", sans-serif; font-size: 24px; line-height: 1.32; }
</style>
</head>
<body>
<main class="booth-wall">
  <svg class="layer" viewBox="0 0 1200 840" aria-hidden="true">
    <defs>
      <linearGradient id="swoosh" x1="0" y1="0" x2="0" y2="1">
        <stop offset="0" stop-color="#2fb3a8"/>
        <stop offset="1" stop-color="#3f5fb0"/>
      </linearGradient>
    </defs>
    <path d="M720 0 C610 220 560 520 690 840 L1200 840 L1200 0 Z" fill="url(#swoosh)"/>
  </svg>

  <svg class="layer" viewBox="0 0 1200 840" role="img" aria-label="Photo of a smiling warehouse worker in a hard hat lifting a cardboard box onto a shelf">
    <defs>
      <linearGradient id="warehouse" x1="0" y1="0" x2="1" y2="1">
        <stop offset="0" stop-color="#7a5a45"/>
        <stop offset="0.5" stop-color="#b08968"/>
        <stop offset="1" stop-color="#2c3550"/>
      </linearGradient>
    </defs>
    <path d="M860 0 C760 160 770 380 930 560 L1200 600 L1200 0 Z" fill="url(#warehouse)"/>
  </svg>

  <svg class="layer" viewBox="0 0 1200 840" aria-hidden="true">
    <path d="M770 840 L770 620 Q772 585 810 575 L975 520 L1150 560 Q1200 575 1200 620 L1200 840 Z" fill="#1b2638"/>
  </svg>

  <div class="signup-badge">
    <div class="signup-badge__strip"></div>
    <div class="signup-badge__card">Sign Up<br>Now</div>
    <div class="signup-badge__roll" role="img" aria-label="Rolled paper scroll illustration"></div>
  </div>

  <h1 class="headline">Enlisting<br>Stakeholder<br>Participation</h1>

  <div class="rule rule--top"></div>
  <div class="title-block">
    <p class="title-block__kicker">First North American</p>
    <h2 class="title-block__main">Product Category Rule (PCR)<br>For Protective Packaging</h2>
  </div>
  <div class="rule rule--bottom"></div>

  <svg class="layer process-arc" viewBox="0 0 1200 840" aria-label="Four-step process">
    <g font-family="Bitter, Georgia, serif" fill="#ffffff">
      <path d="M40 760 A170 170 0 0 1 89.8 639.8 L167.6 717.6 A60 60 0 0 0 150 760 Z" fill="#2b3f8e"/>
      <path d="M89.8 639.8 A170 170 0 0 1 210 590 L210 700 A60 60 0 0 0 167.6 717.6 Z" fill="#2a6f93"/>
      <path d="M210 590 A170 170 0 0 1 330.2 639.8 L252.4 717.6 A60 60 0 0 0 210 700 Z" fill="#2a9a98"/>
      <path d="M330.2 639.8 A170 170 0 0 1 380 760 L270 760 A60 60 0 0 0 252.4 717.6 Z" fill="#2f7fa5"/>
      <g font-size="10.5" text-anchor="middle">
        <text x="110" y="694">PCR</text><text x="110" y="707">Product</text><text x="110" y="720">Category</text><text x="110" y="733">rules</text>
        <text x="165" y="650">LCA</text><text x="165" y="663">Life Cycle</text><text x="165" y="676">Assessment</text>
        <text x="255" y="650">Third</text><text x="255" y="663">Party</text><text x="255" y="676">Verification</text>
        <text x="312" y="704">EPD</text><text x="312" y="717">Registration</text><text x="312" y="730">and Publication</text>
      </g>
      <g stroke="#ffffff" stroke-width="3" fill="#1e2f6e">
        <circle cx="53" cy="695" r="22"/><circle cx="145" cy="603" r="22"/>
        <circle cx="275" cy="603" r="22"/><circle cx="367" cy="695" r="22"/>
      </g>
      <g font-size="20" font-weight="700" text-anchor="middle">
        <text x="53" y="702">01</text><text x="145" y="610">02</text>
        <text x="275" y="610">03</text><text x="367" y="702">04</text>
      </g>
    </g>
  </svg>

  <p class="sponsor">Sponsored by<br>Cellular Foam<br>Alliance Managed<br>by Open Ledger<br>Labs</p>

  <blockquote class="quote">“How EPD Can Move the Dialogue Beyond End-of-Life Disposal to Include Environmental Benchmarks for Product Production &amp; Distribution”</blockquote>
</main>
</body>
</html>
```